Design a Flyer for a Drama Club

OLB Youth Drama Club
Grades: 3rd-Highschool
Thursdays 3:00-5:00 during Ramadan
Cost:$100

Drama club is being offered to Ramadan Campers who are interested in performing a play about "The Keepers of the Orchard". At the end of the month, this play will be performed in front of the community.
We've hired Delia Hostrup an instructor from the Brisbury Youth Theater to give our campers lesson on how to write, direct and act out the play.
Spots are limited and filling up quickly!
For more information contact:
Samira Kendoussi (555) 302-4817
Lujain Marwesh (555) 719-2064

```html
<!DOCTYPE html>
<html lang="en">
<head>
<meta charset="utf-8">
<title>OLB Youth Drama Club</title>
<link rel="stylesheet" href="https://fonts.googleapis.com/css2?family=Playfair+Display:wght@900&family=Libre+Baskerville:wght@400;700&family=Tinos&display=swap">
<style>
  :root {
    --ink: #000000;
    --paper: #ffffff;
    --marquee: #e4de1f;
    --header-cream: #f1e9d6;
    --header-sand: #e2d3b0;
    --ornament-orange: #e0873a;
    --ornament-blue: #3f6c9a;
    --brand-red: #8b1d22;
    --chair-shade: #1b1b1b;
  }
  * { margin: 0; padding: 0; box-sizing: border-box; }
  html, body { width: 816px; height: 1200px; overflow: hidden; background: var(--ink); }
  .flyer {
    position: relative; width: 816px; height: 1200px; overflow: hidden;
    background: var(--ink); color: var(--paper);
    font-family: "Tinos", "Times New Roman", serif;
  }
  .masthead {
    position: absolute; left: 0; top: 0; width: 816px; height: 136px;
    background: linear-gradient(90deg, var(--header-cream) 0%, var(--header-sand) 100%);
  }
  .masthead-ornament {
    position: absolute; right: 0; top: 0; width: 250px; height: 136px;
    background: radial-gradient(circle at 70% 50%, var(--ornament-orange) 0%, var(--ornament-blue) 55%, var(--header-sand) 100%);
    opacity: .75;
  }
  .brand {
    position: absolute; left: 34px; top: 44px;
    display: flex; align-items: center; gap: 18px;
  }
  .brand-dot { width: 48px; height: 48px; border-radius: 50%; background: var(--brand-red); }
  .brand-name {
    font-family: "Libre Baskerville", Georgia, serif; font-weight: 700;
    font-size: 24px; color: var(--brand-red);
  }
  .title {
    position: absolute; left: 0; top: 176px; width: 816px; text-align: center;
    font-family: "Playfair Display", Georgia, serif; font-weight: 900;
    font-size: 68px; line-height: 1; color: var(--marquee); white-space: nowrap;
  }
  .details {
    position: absolute; left: 130px; top: 270px; width: 556px; text-align: center;
    font-family: "Libre Baskerville", Georgia, serif; font-weight: 700;
    font-size: 22px; line-height: 38px; white-space: nowrap;
  }
  .details .cost { color: var(--marquee); }
  .spotlight {
    position: absolute;
    background: radial-gradient(ellipse at var(--origin), rgba(243,210,58,.55) 0%, rgba(243,210,58,.18) 45%, rgba(0,0,0,0) 72%);
  }
  .spotlight-upper { left: 10px; top: 310px; width: 470px; height: 380px; --origin: 15% 20%; }
  .spotlight-lower { left: 300px; top: 830px; width: 516px; height: 370px; --origin: 85% 20%; }
  .about {
    position: absolute; left: 226px; top: 422px; width: 540px; text-align: center;
    font-size: 22px; line-height: 49px; white-space: nowrap;
  }
  .contact-heading {
    position: absolute; left: 0; top: 506px; width: 200px; text-align: center;
    font-family: "Libre Baskerville", Georgia, serif; font-weight: 700;
    font-size: 24px; line-height: 40px;
  }
  .contact {
    position: absolute; left: 9px; width: 200px; height: 200px;
    background: var(--chair-shade);
  }
  .contact-one { top: 660px; }
  .contact-two { top: 940px; }
  .contact-name {
    position: absolute; left: 6px; top: 10px; width: 188px; padding: 6px 0;
    background: var(--paper); color: var(--ink); text-align: center;
    font-family: "Libre Baskerville", Georgia, serif; font-weight: 700; font-size: 17px;
    white-space: nowrap;
  }
  .contact-phone {
    position: absolute; left: 0; top: 100px; width: 200px; text-align: center;
    font-family: "Libre Baskerville", Georgia, serif; font-weight: 700; font-size: 18px;
  }
  .urgency {
    position: absolute; left: 202px; top: 716px; width: 560px; text-align: center;
    font-family: "Libre Baskerville", Georgia, serif; font-weight: 700;
    font-size: 36px; line-height: 53px; color: var(--marquee); white-space: nowrap;
  }
  .instructor {
    position: absolute; left: 222px; top: 952px; width: 330px; text-align: center;
    font-size: 21px; line-height: 50px; white-space: nowrap;
  }
</style>
</head>
<body>
<main class="flyer">
  <header class="masthead">
    <div class="masthead-ornament" role="img" aria-label="Decorative geometric rosette pattern in orange and blue"></div>
    <div class="brand">
      <span class="brand-dot"></span>
      <span class="brand-name">Olive Branch Cultural Association</span>
    </div>
  </header>

  <h1 class="title">OLB Youth Drama Club</h1>

  <div class="details">
    <p>Grades 3rd - High School</p>
    <p>Thursdays 3:00 - 5:00 during Ramadan</p>
    <p class="cost">Cost: $100</p>
  </div>

  <div class="spotlight spotlight-upper" role="img" aria-label="Stage spotlight casting a yellow beam"></div>
  <div class="spotlight spotlight-lower" role="img" aria-label="Stage spotlight casting a yellow beam"></div>

  <p class="about">Drama club is being offered to Ramadan<br>Campers who are interested in performing a<br>play about “The Keepers of the Orchard”.<br>At the end of the month, this play will be<br>performed in front of the community.</p>

  <p class="contact-heading">For more<br>information<br>contact:</p>

  <div class="contact contact-one" role="img" aria-label="Director's chair illustration">
    <p class="contact-name">Samira Kendoussi</p>
    <p class="contact-phone">(555) 302-4817</p>
  </div>
  <div class="contact contact-two" role="img" aria-label="Director's chair illustration">
    <p class="contact-name">Lujain Marwesh</p>
    <p class="contact-phone">(555) 719-2064</p>
  </div>

  <p class="urgency">Spots are limited<br>and filling up quickly!</p>

  <p class="instructor">Learn how to write, direct and<br>act out the play from Delia<br>Hostrup, an instructor from the<br>Brisbury Youth Theater!</p>
</main>
</body>
</html>
```